Business Cards Needed for Innovative Healthcare Marketing Company

We are a marketing company focused on healthcare. Our company is all about rebranding yourself renewing your image and generating results. The phoenix stands for "reborn" or "rising" which we provide new brands for our clients we take their old brands and renew it with creativity and innovation. I am looking for a business card with color dimension. I have attached an example of a card I think has the look and feel of what I am trying to accomplish. I like that the card example has black and grey font colors, I like the font placement and the small logo, I really like the use of the colors on the right those are the colors of my logo. My logo is phoenix so maybe incorporating flames similar to that design. I would like the back a solid color maybe red with an opaque version of the logo and website. As a marketing company I am always open to creative liberty!

Target Market(s)

Doctors and business professionals.

Industry/Entity Type

Marketing

Contact Information for Business Card

Vornaly Health Care Marketing
Marnie Okonski- CEO
#(502)638-2947
email-marnie@vornaly.com
website- vornaly.com

Font styles to use
Sans Serif

Colors
ec1f27
f37122
ffc214
fbed22
fbf289
f04a50

Requirements
Must have
• The logo and required information
Nice to have
• icons by the information
Should not have
• child like font

```html
<!DOCTYPE html>
<html lang="en">
<head>
<meta charset="utf-8">
<title>Vornaly Health Care Marketing – Business Card</title>
<link rel="stylesheet" href="https://fonts.googleapis.com/css2?family=Source+Sans+3:wght@300;400;600&display=swap">
<style>
  :root {
    --stage: #161616;
    --card-front: #f3f3f3;
    --brand-red: #9b1b1f;
    --text-dark: #333333;
    --text-mid: #444444;
    --accent-orange: #f37122;
    --glow-center: #f7941d;
    --glow-mid: #e26a1f;
    --glow-edge: #a8201a;
    --on-dark: #ffffff;
  }
  * { box-sizing: border-box; margin: 0; padding: 0; }
  html, body {
    width: 1200px; height: 900px; overflow: hidden;
    background: var(--stage);
    font-family: "Source Sans 3", sans-serif;
  }
  .canvas { position: relative; width: 1200px; height: 900px; }
  .card {
    position: absolute; top: 184px; height: 491px; border-radius: 12px;
  }
  .card-front {
    left: 299px; width: 301px; background: var(--card-front);
    text-align: center;
  }
  .card-back {
    left: 645px; width: 305px;
    background: radial-gradient(ellipse at 50% 52%, var(--glow-center) 0%, var(--glow-mid) 45%, var(--glow-edge) 100%);
    display: flex; flex-direction: column; align-items: center; justify-content: center;
  }
  .brand-dot {
    position: absolute; left: 50%; top: 92px; width: 46px; height: 46px;
    margin-left: -23px; border-radius: 50%; background: var(--accent-orange);
  }
  .brand-name {
    position: absolute; left: 0; right: 0; top: 192px;
    color: var(--brand-red); font-weight: 300; line-height: 1;
  }
  .brand-name .word { display: block; font-size: 42px; letter-spacing: 1px; }
  .brand-name .tagline { display: block; font-size: 13.5px; letter-spacing: 1px; margin-top: 12px; text-transform: uppercase; }
  .person { position: absolute; left: 0; right: 0; top: 305px; }
  .person-name { font-size: 19px; font-weight: 600; color: var(--brand-red); line-height: 24px; }
  .person-role { font-size: 15px; color: var(--text-mid); line-height: 22px; }
  .contact { position: absolute; left: 0; right: 0; top: 373px; list-style: none; }
  .contact li { font-size: 16px; color: var(--text-dark); line-height: 21px; }
  .back-name {
    color: var(--on-dark); font-weight: 300; font-size: 44px; letter-spacing: 2px; line-height: 1;
  }
</style>
</head>
<body>
<main class="canvas">
  <section class="card card-front" aria-label="Card front">
    <span class="brand-dot" aria-hidden="true"></span>
    <h1 class="brand-name">
      <span class="word">VORNALY</span>
      <span class="tagline">Health Care Marketing</span>
    </h1>
    <div class="person">
      <p class="person-name">Marnie Okonski</p>
      <p class="person-role">CEO</p>
    </div>
    <ul class="contact">
      <li>(502)638-2947</li>
      <li>marnie@vornaly.com</li>
      <li>vornaly.com</li>
    </ul>
  </section>
  <section class="card card-back" aria-label="Card back">
    <p class="back-name">VORNALY</p>
  </section>
</main>
</body>
</html>
```